Revamp Of Landing Page For an Automated AI Voice Agents Agency

here is my current landing page https://app.brightfunnelstudio.example/v2/preview/KXWQPmR4hLsDnTfYvJcA?notrack=true

Please use all my current content and imagery of ai agents in your new design. Make it easy to ready, easy to navigate and easy to understand

I am looking for a SLEEK shiny polished looking website. I like Dark themed sites but am open to see light themed sites too so please dont be shy.

The site should have an Ai Voice Agent Theme about it. Maybe look and feel of futureistic but simple and not intimidating to the average person...

Here are a couple website designs I like for reference:
https://q4t.example/
https://ai-bots.mervinholt.example/
https://chatvexo.example/ai-agents

Target Market(s)

b2b

Industry/Entity Type

AI Voice Agents

Coding

Coded - Design and coding required

Font styles to use
Other font styles liked:
• open

Requirements
Must have
• all elements and content and images used in existing design.
Nice to have
• open
Should not have
• open

```html
<!DOCTYPE html>
<html lang="en">
<head>
<meta charset="utf-8">
<title>Voxelra – AI Voice Agents</title>
<link href="https://fonts.googleapis.com/css2?family=Montserrat:wght@400;500;600;700;800&display=swap" rel="stylesheet">
<style>
:root{
  --hero-bg:#13222d;
  --page-bg:#0a0416;
  --pink:#e91e8c;
  --orange:#ff7a1a;
  --kicker-red:#ff4b2b;
  --white:#ffffff;
  --soft:#d6d0e6;
  --card-border:rgba(150,90,255,.45);
  --faq-bar:#2a2438;
}
*{box-sizing:border-box;margin:0;padding:0}
html,body{width:1200px;height:4669px;overflow:hidden}
body{position:relative;background:var(--page-bg);font-family:'Montserrat',sans-serif;color:var(--white)}
.abs{position:absolute}

/* shared */
.brand{display:flex;align-items:center;gap:10px;font-weight:600;letter-spacing:3px;color:var(--white)}
.brand-dot{width:22px;height:22px;border-radius:50%;border:2px solid var(--white)}
.btn{display:block;height:33px;line-height:33px;border-radius:4px;font-size:12px;font-weight:500;color:var(--white);
  white-space:nowrap;text-align:center;width:205px;background:linear-gradient(90deg,#6a22e8,#e91e8c)}
.btn.pill{border-radius:17px}
.lead-copy{font-size:12.5px;line-height:19px;color:var(--soft)}
.lead-copy u{color:var(--pink)}
.section-h{font-weight:800;font-size:31px;line-height:38px;text-transform:uppercase;color:var(--white);letter-spacing:-.3px}
.center{left:0;width:1200px;text-align:center}
.kicker{font-size:14px;font-weight:500;letter-spacing:.5px;text-transform:uppercase}

/* hero */
.hero{left:0;top:0;width:1200px;height:625px;background:var(--hero-bg)}
.hero-title{left:141px;top:162px;font-size:34px;line-height:48px;font-weight:800;letter-spacing:-1px;
  background:linear-gradient(90deg,#7a3cff,#d42bb8 70%,#ff2d7a);-webkit-background-clip:text;background-clip:text;color:transparent}
.hero-sub{left:141px;top:262px;width:360px;font-size:14.5px;line-height:23px;font-weight:600}
.hero-photo{left:598px;top:63px;width:472px;height:472px;border-radius:50%;border:4px solid var(--white);
  background:radial-gradient(circle at 55% 45%,#2f6f9a,#163a55 55%,#0b1a29)}

/* workforce */
.workforce{left:0;top:625px;width:1200px;height:1010px;
  background:radial-gradient(ellipse at 70% 20%,#2a0d5e,transparent 60%),radial-gradient(ellipse at 20% 70%,#1e0848,transparent 60%),#0c0520}
.workforce-title{left:141px;top:675px}
.workforce-copy{left:141px;top:904px;width:250px;font-size:12px}
.agent-card{width:290px;height:437px;border:1px solid var(--card-border);border-radius:4px;text-align:center;padding:0 14px;
  background:linear-gradient(180deg,#1d0d45 0%,#120830 60%,#0d0624)}
.agent-photo{position:absolute;left:8px;top:8px;width:272px;height:175px}
.agent-icon{position:absolute;left:115px;top:150px;width:60px;height:60px;border-radius:50%;border:3px solid rgba(255,255,255,.7);display:flex;align-items:center;justify-content:center}
.agent-name{margin-top:228px;font-size:15.5px;font-weight:500}
.agent-tag{margin-top:12px;font-size:11px;line-height:18px;font-weight:700}
.agent-text{font-size:11px;line-height:18px;color:var(--soft)}
.agent-text.first{margin-top:14px}

/* wish */
.wish-band{left:0;top:1640px;width:1200px;height:470px;
  background:radial-gradient(ellipse at 50% 70%,rgba(60,80,255,.55),transparent 60%),radial-gradient(ellipse at 50% 100%,rgba(120,60,255,.35),transparent 70%)}
.wish-kicker{top:1767px;color:var(--kicker-red)}
.wish-title{top:1798px;font-size:30px}
.wish-line{top:1862px;font-size:15px;font-weight:600}
.wish-body{top:1893px;left:270px;width:660px;text-align:center;font-size:15px;line-height:24px;font-weight:600}

/* features */
.never-title{top:2128px;font-size:30px}
.feature{width:260px;text-align:center}
.feature-ring{width:84px;height:84px;margin:0 auto;border-radius:50%;display:flex;align-items:center;justify-content:center}
.feature-name{margin-top:27px;font-size:15px;font-weight:600;letter-spacing:.5px}
.feature-text{margin-top:14px;font-size:11.5px;line-height:18px;color:var(--soft)}

/* hire */
.hire-title{left:141px;top:2550px}
.hire-kicker{left:141px;top:2652px;color:var(--orange);font-weight:600}
.hire-sub{left:141px;top:2680px;width:440px;font-size:20px;line-height:29px;font-weight:600}
.hire-copy{left:141px;top:2813px;width:340px}
.hire-art{left:598px;top:2493px;width:490px;height:444px;
  background:radial-gradient(ellipse at 55% 50%,rgba(255,110,40,.55),rgba(180,40,40,.25) 40%,transparent 70%)}

/* promise */
.stars-card{left:141px;top:3077px;width:290px;height:350px;border:1px solid rgba(150,90,255,.35);text-align:center;
  background:radial-gradient(ellipse at 50% 50%,#2a0f55,#0e0626 75%)}
.stars-text{margin-top:48px;font-size:23px;line-height:32px;font-weight:600;text-transform:uppercase;padding:0 20px}
.stars{margin-top:14px;display:flex;justify-content:center;gap:8px}
.promise-title{left:453px;top:3085px;width:606px;text-align:center;font-size:30px}
.promise-card{top:3171px;width:290px;height:256px;border:1px solid rgba(120,140,255,.35);text-align:center}
.promise-card.green{left:455px;background:radial-gradient(ellipse at 50% 40%,#0f3a2a,#07140f 75%)}
.promise-card.blue{left:769px;background:radial-gradient(ellipse at 50% 40%,#0d2a6a,#071030 75%)}
.promise-icon{width:80px;height:80px;margin:40px auto 0;border-radius:50%;display:flex;align-items:center;justify-content:center;border:3px solid rgba(255,255,255,.8)}
.promise-name{margin-top:32px;font-size:15px;line-height:19px;font-weight:600}
.promise-text{margin-top:12px;font-size:11.5px;line-height:18px;color:var(--soft)}

/* faq */
.faq-title{top:3556px;font-size:30px}
.faq-item{left:263px;width:674px}
.faq-q{height:40px;background:var(--faq-bar);display:flex;align-items:center;gap:16px;padding-left:10px;font-size:14.5px;font-weight:600}
.faq-mark{width:24px;height:24px;border-radius:50%;border:2px solid #8a6cff;background:#3a2a6a}
.faq-a{padding:16px 0 0 28px;margin-left:22px;border-left:2px solid #5a4a8a;font-size:11.5px;line-height:21px;color:var(--soft)}

/* final */
.final-title{top:4058px;font-size:30px;line-height:39px}
.final-copy{left:330px;top:4254px;width:540px;text-align:center}

/* footer */
.footer-brand{left:0;width:1200px;top:4388px;justify-content:center;font-size:40px;letter-spacing:5px}
.footer-brand .brand-dot{width:38px;height:38px;border-width:3px}
.footer-rule{left:141px;top:4467px;width:918px;height:1px;background:rgba(255,255,255,.2)}
.copyright{left:141px;top:4484px;font-size:11px;color:var(--soft)}
.disclaimer-links{right:141px;top:4484px;font-size:11px;color:var(--soft)}
.guarantee-bar{left:141px;top:4522px;width:918px;height:33px;background:linear-gradient(90deg,#8a2be2,#ff1e8c);font-size:11px;line-height:33px;text-align:center;white-space:nowrap}
.contact-line{top:4574px;font-size:11px;color:var(--soft)}
.legal{top:4624px;font-size:11px;line-height:18px;color:var(--soft)}
</style>
</head>
<body>

<!-- HERO -->
<section class="abs hero"></section>
<div class="abs brand" style="left:141px;top:22px;font-size:24px"><span>VOXELRA</span><span class="brand-dot"></span></div>
<h1 class="abs hero-title">AI VOICE AGENTS<br>THAT ANSWER CALLS,</h1>
<p class="abs hero-sub">Book Appts, Send Emails, Text Messages, Follow Up Reminders, Transfer Calls &amp; More For You 24 Hours 7 Days A Week!</p>
<a class="abs btn pill" style="left:141px;top:359px">Get An Instant Free Demo</a>
<p class="abs lead-copy" style="left:141px;top:404px;width:375px">We Will Create An Ai Agent Customized For Your Business At No Cost. Simply <u>Click The Button</u> Above And Your Very Own Ai Agent Will Be Calling You In Just A Couple Minutes. Experience The Magic And Get Ready To Be Very Impressed!</p>
<div class="abs hero-photo" role="img" aria-label="Photo of a human-like AI agent with a headset working at a laptop"></div>

<!-- WORKFORCE -->
<section class="abs workforce"></section>
<h2 class="abs section-h workforce-title">Meet Your<br>New AI-<br>Powered<br>Workforce</h2>
<a class="abs btn" style="left:141px;top:852px">Get An Instant Free Demo</a>
<p class="abs lead-copy workforce-copy">We Will Create An Ai Agent Customized For Your Business At No Cost. Simply <u>Click The Button</u> Above And Your Very Own Ai Agent Will Be Calling You In Just A Couple Minutes. Experience The Magic And Get Ready To Be Very Impressed!</p>

<article class="abs agent-card" style="left:453px;top:671px">
  <div class="agent-photo" role="img" aria-label="Photo of the AI sales agent at an office desk" style="background:linear-gradient(160deg,#9aa3ad,#4c5661 60%,#2a2f36)"></div>
  <div class="agent-icon" style="background:radial-gradient(circle,#b03cff,#5a16b8)"><svg width="26" height="26" viewBox="0 0 24 24" fill="none" stroke="#fff" stroke-width="2"><path d="M4 5h16v10H9l-5 4z"/></svg></div>
  <h3 class="agent-name">Ai Sales Agent</h3>
  <p class="agent-text first">Brian will take your inbound sales calls. Will give all detailed information to the customer, answer questions in a normal conversational tone and can book sales appointments or transfer hot prospects to a human to close the sale.</p>
</article>

<article class="abs agent-card" style="left:769px;top:671px;background:linear-gradient(180deg,#2a0d55,#3a0e60 60%,#1a0836)">
  <div class="agent-photo" role="img" aria-label="Photo of the AI receptionist wearing a headset" style="background:linear-gradient(160deg,#3fb8c8,#1e5f7a 60%,#143043)"></div>
  <div class="agent-icon" style="background:radial-gradient(circle,#ff4fb0,#c0137a)"><svg width="26" height="26" viewBox="0 0 24 24" fill="none" stroke="#fff" stroke-width="2"><path d="M5 4h5l2 5-3 2a11 11 0 0 0 4 4l2-3 5 2v5a2 2 0 0 1-2 2A17 17 0 0 1 3 6a2 2 0 0 1 2-2z"/></svg></div>
  <h3 class="agent-name">Ai Receptionist</h3>
  <p class="agent-tag">Takes Overflow and After Hours Calls or Can Take Calls 24/7 &amp; Transfer To Appropriate Dept.</p>
  <p class="agent-text">Cody handles all your calls 24/7. You can also set him to only take overflow calls and after hours. He can send emails and sms messages and even book appointments over the call</p>
</article>

<article class="abs agent-card" style="left:141px;top:1137px;background:linear-gradient(180deg,#140a30,#0d1a22 70%,#0b1a14)">
  <div class="agent-photo" role="img" aria-label="Photo of the AI appointment setter robot with a headset" style="background:linear-gradient(160deg,#7e8a90,#3c4a52 60%,#1c2328)"></div>
  <div class="agent-icon" style="background:radial-gradient(circle,#3ee06a,#138a34)"><svg width="26" height="26" viewBox="0 0 24 24" fill="none" stroke="#fff" stroke-width="2"><rect x="4" y="5" width="16" height="15" rx="2"/><path d="M4 10h16M9 3v4M15 3v4"/></svg></div>
  <h3 class="agent-name">Ai Appointment Setter</h3>
  <p class="agent-tag">Book Appts &amp; Reservations On Auto Pilot</p>
  <p class="agent-text">Bobby offers business advice, helps brainstorm ideas, and provides insights on growth tactics to support your entrepreneurial journey.</p>
</article>

<article class="abs agent-card" style="left:453px;top:1137px">
  <div class="agent-photo" role="img" aria-label="Photo of the AI lead qualifier robot beside a person at a laptop" style="background:linear-gradient(160deg,#2f6aa0,#163a5e 60%,#0c1d33)"></div>
  <div class="agent-icon" style="background:radial-gradient(circle,#3c6bff,#1a2fc0)"><svg width="26" height="26" viewBox="0 0 24 24" fill="none" stroke="#fff" stroke-width="2"><circle cx="12" cy="8" r="4"/><path d="M4 21a8 8 0 0 1 16 0"/></svg></div>
  <h3 class="agent-name">Ai Lead Qualifier</h3>
  <p class="agent-tag">Conversate With Prospects To Qualify Before Handing Over To Sales Team</p>
  <p class="agent-text">All of our ai agents gather information and qualify leads. If they are interested in the services on the call then our ai agents will assist them with booking an appointment with our sales team over the call.</p>
</article>

<article class="abs agent-card" style="left:769px;top:1137px;background:linear-gradient(180deg,#150a30,#1a1020 60%,#2a1a08)">
  <div class="agent-photo" role="img" aria-label="Photo of the AI follow up robot in a bright office" style="background:linear-gradient(160deg,#6fb6c8,#34707f 60%,#1a3840)"></div>
  <div class="agent-icon" style="background:radial-gradient(circle,#ffb23a,#e06a0c)"><svg width="26" height="26" viewBox="0 0 24 24" fill="none" stroke="#fff" stroke-width="2"><path d="M6 16V11a6 6 0 0 1 12 0v5l2 2H4z"/><path d="M10 21h4"/></svg></div>
  <h3 class="agent-name">Ai Follow Up Reminders</h3>
  <p class="agent-tag">Calls, Sends SMS &amp; Email Reminders</p>
  <p class="agent-text">Sam handles all the follow up calls, appt reminders and sends out the email and sms reminders too.</p>
</article>

<!-- WISH -->
<div class="abs wish-band" role="img" aria-label="Glowing blue digital wave background"></div>
<p class="abs center kicker wish-kicker">Install The Power Of AI For Your Business</p>
<h2 class="abs center section-h wish-title">Your Wish Is Their Command</h2>
<p class="abs center wish-line">Your New Ai Agents Will Never Call In Sick And Will Never Complain!</p>
<p class="abs wish-body">With your new team of AI Agents, handling inbound calls, sending emails and sms messages, booking appointments and handling customer service inquiries is going to save you a ton of time and money.</p>

<!-- FEATURES -->
<h2 class="abs center section-h never-title">An Employee That Never Gets Sick!</h2>
<div class="abs feature" style="left:216px;top:2201px">
  <div class="feature-ring" style="background:radial-gradient(circle,#0f3a22,#07140e);box-shadow:0 0 0 3px #1fb35a inset"><svg width="36" height="36" viewBox="0 0 24 24" fill="none" stroke="#fff" stroke-width="1.6"><circle cx="12" cy="12" r="5"/><path d="M12 2v5M12 17v5M2 12h5M17 12h5"/></svg></div>
  <h3 class="feature-name">TRAINED IN SECONDS</h3>
  <p class="feature-text">Learns Your Entire Website<br>In Seconds</p>
</div>
<div class="abs feature" style="left:470px;top:2201px">
  <div class="feature-ring" style="background:radial-gradient(circle,#3a0f3a,#140714);box-shadow:0 0 0 3px #c02a9a inset"><svg width="36" height="36" viewBox="0 0 24 24" fill="none" stroke="#fff" stroke-width="1.6"><circle cx="12" cy="12" r="9"/><path d="M3 12h18M12 3a14 14 0 0 1 0 18M12 3a14 14 0 0 0 0 18"/></svg></div>
  <h3 class="feature-name">WORLDWIDE</h3>
  <p class="feature-text">Works Anywhere In<br>The Globe</p>
</div>
<div class="abs feature" style="left:722px;top:2201px">
  <div class="feature-ring" style="background:radial-gradient(circle,#3a220a,#140b04);box-shadow:0 0 0 3px #e0831a inset"><svg width="36" height="36" viewBox="0 0 24 24" fill="none" stroke="#fff" stroke-width="1.6"><circle cx="12" cy="9" r="4"/><path d="M5 21a7 7 0 0 1 14 0"/></svg></div>
  <h3 class="feature-name">USER-FRIENDLY</h3>
  <p class="feature-text">Your Ai Agents Sound As If<br>They're Real Humans</p>
</div>

<!-- HIRE -->
<h2 class="abs section-h hire-title">Our AI Agents<br>Our Ready To Be Hired</h2>
<p class="abs kicker hire-kicker">Lightning-Fast Responses</p>
<p class="abs hire-sub">Instant answers, no coffee, bathroom<br>or lunch breaks needed</p>
<a class="abs btn" style="left:141px;top:2759px">Get An Instant Free Demo</a>
<p class="abs lead-copy hire-copy">We Will Create An Ai Agent Customized For Your Business At No Cost. Simply <u>Click The Button</u> Above And Your Very Own Ai Agent Will Be Calling You In Just A Couple Minutes. Experience The Magic And Get Ready To Be Very Impressed!</p>
<div class="abs hire-art" role="img" aria-label="Illustration of a glowing lightning bolt with the words lightning responses"></div>

<!-- PROMISE -->
<div class="abs stars-card">
  <p class="stars-text">After our customers have a conversation with their new AI voice agent they give us 5 stars!</p>
  <div class="stars">
    <svg width="28" height="28" viewBox="0 0 24 24"><path fill="#ff8a1a" d="M12 2l3 7h7l-5.5 4.5 2 7.5L12 17l-6.5 4 2-7.5L2 9h7z"/></svg>
    <svg width="28" height="28" viewBox="0 0 24 24"><path fill="#ff8a1a" d="M12 2l3 7h7l-5.5 4.5 2 7.5L12 17l-6.5 4 2-7.5L2 9h7z"/></svg>
    <svg width="28" height="28" viewBox="0 0 24 24"><path fill="#ff8a1a" d="M12 2l3 7h7l-5.5 4.5 2 7.5L12 17l-6.5 4 2-7.5L2 9h7z"/></svg>
    <svg width="28" height="28" viewBox="0 0 24 24"><path fill="#ff8a1a" d="M12 2l3 7h7l-5.5 4.5 2 7.5L12 17l-6.5 4 2-7.5L2 9h7z"/></svg>
    <svg width="28" height="28" viewBox="0 0 24 24"><path fill="#ff8a1a" d="M12 2l3 7h7l-5.5 4.5 2 7.5L12 17l-6.5 4 2-7.5L2 9h7z"/></svg>
  </div>
</div>
<h2 class="abs section-h promise-title">Our Promise To You:</h2>
<div class="abs promise-card green">
  <div class="promise-icon" style="background:#1a9a3a"><svg width="36" height="36" viewBox="0 0 24 24" fill="none" stroke="#fff" stroke-width="1.8"><rect x="4" y="5" width="16" height="15" rx="2"/><path d="M4 10h16M9 3v4M15 3v4"/><text x="12" y="18" font-size="6" fill="#fff" stroke="none" text-anchor="middle" font-family="Montserrat,sans-serif" font-weight="700">14</text></svg></div>
  <h3 class="promise-name">14-DAY MONEY-BACK<br>GUARANTEE*</h3>
</div>
<div class="abs promise-card blue">
  <div class="promise-icon" style="background:#1e4fe0"><svg width="36" height="36" viewBox="0 0 24 24" fill="none" stroke="#fff" stroke-width="1.8"><circle cx="12" cy="12" r="8"/><text x="12" y="14.5" font-size="6" fill="#fff" stroke="none" text-anchor="middle" font-family="Montserrat,sans-serif" font-weight="700">24</text></svg></div>
  <h3 class="promise-name">24/7 CUSTOMER<br>SUPPORT</h3>
  <p class="promise-text">Often praised for our friendly<br>&amp; helpful support team</p>
</div>

<!-- FAQ -->
<h2 class="abs center section-h faq-title">Do You Have Questions?</h2>
<div class="abs faq-item" style="top:3628px">
  <div class="faq-q"><span class="faq-mark"></span>What exactly are the AI Voice Agents?</div>
  <p class="faq-a">AI Voice Agents are specialized human sounding bots, having smart and masterful conversations and each is expertly trained in seconds for a specific business function.</p>
</div>
<div class="abs faq-item" style="top:3746px">
  <div class="faq-q"><span class="faq-mark"></span>How will these AI Voice Agents benefit</div>
  <p class="faq-a">Ai Voice Agents Answer Calls, Book Appts, Send Emails, Text Messages, Follow Up Reminders &amp; More For You 24/7!</p>
</div>
<div class="abs faq-item" style="top:3862px">
  <div class="faq-q"><span class="faq-mark"></span>Are they easy to use?</div>
  <p class="faq-a">We provide a done for you service. We create your AI Voice Agent and launch it within days!</p>
</div>

<!-- FINAL CTA -->
<h2 class="abs center section-h final-title">These AI Agents Can Help<br>Your Business Tremendously.<br>Imagine The Possibilities</h2>
<a class="abs btn" style="left:498px;top:4197px">Get An Instant Free Demo</a>
<p class="abs lead-copy final-copy">We Will Create An Ai Agent Customized For Your Business At No Cost. Simply <u>Click The Button</u> Above And Your Very Own Ai Agent Will Be Calling You In Just A Couple Minutes. Experience The Magic And Get Ready To Be Very Impressed!</p>

<!-- FOOTER -->
<div class="abs brand footer-brand"><span>VOXELRA</span><span class="brand-dot"></span></div>
<div class="abs footer-rule"></div>
<p class="abs copyright">© 2025 Voxelra. All rights reserved.</p>
<p class="abs disclaimer-links">Disclaimer: Privacy | Terms &amp; Conditions | Earnings &amp; Products Disclaimer</p>
<p class="abs guarantee-bar">*14-Day Money Back Guarantee Terms: If you use the ai agents and you're not happy. Then you can contact us in the first 14 days for a full refund.</p>
<p class="abs center contact-line">Do you have questions about ( ) Please email ( )</p>
<p class="abs center legal">IMPORTANT: This site is not a part of the Linkspace website or Linkspace Inc. Additionally,<br>this site is NOT endorsed by Linkspace in any way. LINKSPACE is a trademark of LINKSPACE, Inc.</p>

</body>
</html>
```